professional business card

Professional business card with logo on one side, and underneath logo list:
- power
-data
-fibre optic
-isolar

On other side:
Marcus Webb
Owner
MOB 0432 958 720
marcus@vorn.com.au
www.vornelectrical.com.au

Please edit logo to just leave VORN

```html
<!DOCTYPE html>
<html lang="en">
<head>
<meta charset="utf-8">
<title>VORN business cards</title>
<link href="https://fonts.googleapis.com/css2?family=Lato:wght@300;400;700&display=swap" rel="stylesheet">
<style>
  :root {
    --teal: #1a9ea6;
    --page: #2a2c30;
    --card-light: #ffffff;
    --card-dark: #0b0b0c;
    --ink-light: #7a7a7a;
    --ink-dark: #8a8a8a;
    --band-text: #e8f6f7;
  }
  * { box-sizing: border-box; margin: 0; padding: 0; }
  html, body { width: 1200px; height: 900px; overflow: hidden; }
  body {
    background: var(--page);
    font-family: "Lato", sans-serif;
    display: flex;
    flex-direction: column;
    align-items: center;
    justify-content: center;
    gap: 50px;
  }
  .card {
    position: relative;
    width: 620px;
    height: 365px;
    border-radius: 24px;
    overflow: hidden;
    box-shadow: 0 14px 30px rgba(0,0,0,0.45);
  }
  .card--light { background: var(--card-light); color: var(--ink-light); }
  .card--dark { background: var(--card-dark); color: var(--ink-dark); }

  .brand {
    position: absolute;
    right: 50px;
    top: 86px;
    font-weight: 700;
    font-size: 92px;
    line-height: 1;
    letter-spacing: 2px;
    color: var(--teal);
  }
  .holder {
    position: absolute;
    left: 44px;
    top: 138px;
  }
  .holder__name {
    font-weight: 400;
    font-size: 25px;
    letter-spacing: -0.5px;
    line-height: 1;
    white-space: nowrap;
  }
  .holder__role {
    font-size: 11px;
    color: var(--teal);
    letter-spacing: 0.5px;
    margin-top: 4px;
    line-height: 1;
  }
  .divider {
    position: absolute;
    left: 100px;
    right: 0;
    top: 180px;
    height: 2px;
    background: var(--teal);
  }
  .contacts {
    position: absolute;
    left: 30px;
    top: 192px;
    list-style: none;
  }
  .contacts li {
    display: flex;
    align-items: center;
    gap: 8px;
    font-size: 14px;
    height: 22px;
    white-space: nowrap;
  }
  .contacts svg { width: 11px; height: 11px; flex: none; }
  .services {
    position: absolute;
    left: 0;
    right: 0;
    bottom: 0;
    height: 48px;
    background: var(--teal);
    color: var(--band-text);
    display: flex;
    align-items: center;
    padding-left: 56px;
    font-size: 16px;
    letter-spacing: 0.3px;
    gap: 14px;
  }
  .services .sep { opacity: 0.9; }
</style>
</head>
<body>

  <section class="card card--light" aria-label="Business card, light version">
    <div class="brand">VORN</div>
    <div class="holder">
      <div class="holder__name">MARCUS WEBB</div>
      <div class="holder__role">OWNER</div>
    </div>
    <div class="divider"></div>
    <ul class="contacts">
      <li><svg viewBox="0 0 12 12"><rect x="3" y="0.5" width="6" height="11" rx="1" fill="none" stroke="#1a9ea6" stroke-width="1.3"/></svg>0432 958 720</li>
      <li><svg viewBox="0 0 12 12"><rect x="1.5" y="1.5" width="9" height="9" rx="1" fill="none" stroke="#1a9ea6" stroke-width="1.3"/></svg>9371 2846</li>
      <li><svg viewBox="0 0 12 12"><rect x="0.5" y="0.5" width="11" height="11" rx="1.5" fill="#1a9ea6"/><path d="M3 6l2 2 4-4" fill="none" stroke="#fff" stroke-width="1.4"/></svg>marcus@vorn.com.au</li>
      <li><svg viewBox="0 0 12 12"><circle cx="6" cy="6" r="5.5" fill="#1a9ea6"/><path d="M1 6h10M6 1v10" stroke="#fff" stroke-width="0.8"/></svg>www.vornelectrical.com.au</li>
    </ul>
    <div class="services">
      <span>POWER</span><span class="sep">|</span><span>DATA</span><span class="sep">|</span><span>FIBRE OPTIC</span><span class="sep">|</span><span>SOLAR</span>
    </div>
  </section>

  <section class="card card--dark" aria-label="Business card, dark version">
    <div class="brand">VORN</div>
    <div class="holder">
      <div class="holder__name">MARCUS WEBB</div>
      <div class="holder__role">OWNER</div>
    </div>
    <div class="divider"></div>
    <ul class="contacts">
      <li><svg viewBox="0 0 12 12"><rect x="3" y="0.5" width="6" height="11" rx="1" fill="none" stroke="#1a9ea6" stroke-width="1.3"/></svg>0432 958 720</li>
      <li><svg viewBox="0 0 12 12"><rect x="1.5" y="1.5" width="9" height="9" rx="1" fill="none" stroke="#1a9ea6" stroke-width="1.3"/></svg>9371 2846</li>
      <li><svg viewBox="0 0 12 12"><rect x="0.5" y="0.5" width="11" height="11" rx="1.5" fill="#1a9ea6"/><path d="M3 6l2 2 4-4" fill="none" stroke="#0b0b0c" stroke-width="1.4"/></svg>marcus@vorn.com.au</li>
      <li><svg viewBox="0 0 12 12"><circle cx="6" cy="6" r="5.5" fill="#1a9ea6"/><path d="M1 6h10M6 1v10" stroke="#0b0b0c" stroke-width="0.8"/></svg>www.vornelectrical.com.au</li>
    </ul>
    <div class="services">
      <span>POWER</span><span class="sep">|</span><span>DATA</span><span class="sep">|</span><span>FIBRE OPTIC</span><span class="sep">|</span><span>SOLAR</span>
    </div>
  </section>

</body>
</html>
```